New Business Card Design Project

Hi there

Could you please make a design that is soft and appealing to people who would purchase gemstones, buy healing jewellery, seek counselling, may seek energy healing and/or learn English. Essentially I'm looking for something with a soft human design. Please incorporate the logo and select font that can be easily read and softer images in the background - but not too busy. I would like it double sided as well.

Optional: Elements could include gemstones, feathers, plants and images that are happy and calming.

Target Market(s)

People into alternative health, those from non-English speaking backgrounds, businesses

Contact Information for Business Card

Leo Marsdon
Mobile: 0412 586 239, Facebook and Instagram Logos,
ABN: 51 742 118 603 (Australian Business Number - small at the bottom)

Requirements
Must have
• My project must have:
- Tranquil Harbor logo
- Symbols that represent the 4 main services: 1. Gemstones/jewellery, 2. counselling, 3. meditation/energy healing, 4. education
Nice to have
• Clear and easy to read.

```html
<!DOCTYPE html>
<html lang="en">
<head>
<meta charset="utf-8">
<title>Tranquil Harbor – Business Card</title>
<link rel="stylesheet" href="https://fonts.googleapis.com/css2?family=Marcellus&family=Philosopher:wght@700&family=Roboto+Condensed&family=Arimo&display=swap">
<style>
  :root {
    --backdrop: #2b2b2b;
    --paper: #ececeb;
    --brand-green: #3f9a3c;
    --brand-teal: #1f8f7a;
    --tile-top: #5fb85a;
    --tile-bottom: #2f9648;
    --ink: #3a3a3a;
    --back-green: #6a9f45;
    --back-green-light: #79ad52;
    --white: #f4f4f0;
  }
  * { box-sizing: border-box; margin: 0; padding: 0; }
  html, body { width: 1200px; height: 896px; overflow: hidden; }
  body { background: var(--backdrop); position: relative; }

  .card {
    position: absolute;
    left: 353px;
    width: 486px;
    height: 277px;
    box-shadow: 0 8px 22px rgba(0,0,0,.55);
    overflow: hidden;
  }
  .card--front { top: 160px; background: var(--paper); }
  .card--back { top: 469px; }

  /* Front */
  .brand-mark { position: absolute; left: 31px; top: 30px; width: 108px; text-align: center; }
  .brand-mark__dot {
    width: 34px; height: 34px; margin: 0 auto 6px;
    border: 2px solid var(--brand-teal); border-radius: 50%;
  }
  .brand-mark__name {
    font-family: "Marcellus", serif; color: var(--brand-teal);
    font-size: 17px; line-height: 17px; letter-spacing: .5px;
  }
  .holder {
    position: absolute; left: 31px; top: 128px;
    font-family: "Philosopher", sans-serif; font-weight: 700;
    font-size: 18px; color: var(--brand-green);
  }
  .holder__rule {
    position: absolute; left: 31px; top: 154px;
    width: 21px; height: 3px; background: var(--brand-teal);
  }
  .contacts {
    position: absolute; left: 31px; top: 170px; list-style: none;
    font-family: "Arimo", sans-serif; font-size: 11px; color: var(--ink);
  }
  .contacts li { display: flex; align-items: center; height: 14px; }
  .contacts svg { width: 9px; height: 9px; margin-right: 8px; flex: none; }
  .abn {
    position: absolute; left: 31px; top: 233px;
    font-family: "Arimo", sans-serif; font-size: 11px; color: var(--ink);
  }
  .services { position: absolute; left: 210px; top: 181px; display: flex; gap: 8px; }
  .service {
    width: 55px; height: 66px; border-radius: 4px;
    background: linear-gradient(var(--tile-top), var(--tile-bottom));
    display: flex; flex-direction: column; align-items: center;
    padding-top: 10px; color: var(--white);
  }
  .service svg { width: 28px; height: 28px; }
  .service__label {
    margin-top: auto; margin-bottom: 4px;
    font-family: "Roboto Condensed", sans-serif; font-size: 10.5px;
  }
  .front-band {
    position: absolute; left: 0; bottom: 0; width: 100%; height: 6px;
    background: var(--brand-green);
  }

  /* Back */
  .back-scene {
    position: absolute; inset: 0;
    background: radial-gradient(ellipse at 50% 60%, var(--back-green-light), var(--back-green) 70%);
  }
  .back-brand { position: absolute; left: 0; top: 68px; width: 100%; text-align: center; }
  .back-brand__dot {
    width: 70px; height: 70px; margin: 0 auto 14px;
    border: 3px solid var(--white); border-radius: 50%;
  }
  .back-brand__name {
    font-family: "Marcellus", serif; color: var(--white);
    font-size: 34px; line-height: 36px; letter-spacing: 1px;
  }
</style>
</head>
<body>

<section class="card card--front" aria-label="Business card front">
  <div class="brand-mark">
    <div class="brand-mark__dot"></div>
    <div class="brand-mark__name">TRANQUIL<br>HARBOR</div>
  </div>

  <h1 class="holder">Leo Marsdon</h1>
  <div class="holder__rule"></div>

  <ul class="contacts">
    <li><svg viewBox="0 0 10 10"><rect x="2.5" y="0.5" width="5" height="9" rx="1" fill="none" stroke="#3f9a3c" stroke-width="1.2"/></svg>0412 586 239</li>
    <li><svg viewBox="0 0 10 10"><circle cx="5" cy="5" r="5" fill="#3f9a3c"/></svg>/TranquilHarbor</li>
    <li><svg viewBox="0 0 10 10"><circle cx="5" cy="5" r="5" fill="#3f9a3c"/></svg>@TranquilHarbor</li>
    <li><svg viewBox="0 0 10 10"><rect x="0.5" y="2" width="9" height="6" fill="#3f9a3c"/><path d="M0.5 2 L5 5.5 L9.5 2" fill="none" stroke="#ececeb" stroke-width="1"/></svg>info@TranquilHarbor.com</li>
  </ul>
  <p class="abn">ABN: 51 742 118 603</p>

  <div class="services">
    <div class="service">
      <svg viewBox="0 0 28 28" fill="none" stroke="#f4f4f0" stroke-width="1.4" stroke-linejoin="round">
        <path d="M6 10 L10 5 H18 L22 10 L14 24 Z M6 10 H22 M10 5 L12 10 L14 24 M18 5 L16 10 L14 24"/>
      </svg>
      <span class="service__label">Jewellery</span>
    </div>
    <div class="service">
      <svg viewBox="0 0 28 28" fill="none" stroke="#f4f4f0" stroke-width="1.6" stroke-linejoin="round">
        <path d="M14 23 C4 16 3 11 5 8 C7 5 11 5 14 9 C17 5 21 5 23 8 C25 11 24 16 14 23 Z"/>
      </svg>
      <span class="service__label">Counselling</span>
    </div>
    <div class="service">
      <svg viewBox="0 0 28 28" fill="#f4f4f0">
        <path d="M14 4 C17 8 17 12 14 15 C11 12 11 8 14 4 Z"/>
        <path d="M5 10 C9 10 12 12 13 16 C9 16 6 14 5 10 Z"/>
        <path d="M23 10 C19 10 16 12 15 16 C19 16 22 14 23 10 Z"/>
        <rect x="6" y="19" width="16" height="2" rx="1"/>
      </svg>
      <span class="service__label">Meditation</span>
    </div>
    <div class="service">
      <svg viewBox="0 0 28 28" fill="#f4f4f0">
        <path d="M2 11 L14 6 L26 11 L14 16 Z"/>
        <path d="M7 14 V19 C10 21 18 21 21 19 V14 L14 17 Z"/>
        <rect x="23.3" y="11" width="1.2" height="7"/>
      </svg>
      <span class="service__label">Education</span>
    </div>
  </div>

  <div class="front-band"></div>
</section>

<section class="card card--back" aria-label="Business card back">
  <div class="back-scene" role="img" aria-label="Soft green-tinted photograph of crystals, gemstones, leaves and a feather"></div>
  <div class="back-brand">
    <div class="back-brand__dot"></div>
    <div class="back-brand__name">TRANQUIL<br>HARBOR</div>
  </div>
</section>

</body>
</html>
```